Business Card Design Project

Please create a custom business card for Plume analytics. The logo is attached to this brief.

Address :
CEO : Baptiste Lorand
Mobile : +33641927508
14 rue Véronèse
75013 Paris
France

Reason: Sorry wrong logo. I will update asap

Hi, Sorry, I post the wrong file. I just update the correct logo. If you can integrate some charts as background it will be nice

Hi Everybody Please make it beautifull, clean, soft like pebble designs does to create their product. I want somewhere to show in a beautifull way some datavisualization charts. Not to much, but try to find a way to design it beautifull with less. Get inspire by datavisualization : http://www.morvelkit.com/48207-clean-vector-infographic-and-data-visualization-design-elements-03/

Target Market(s)

B to B
Customers are accountant, CPA, finance departement

Industry/Entity Type

Business

Font styles to use
Sans Serif

Requirements
Must have
• I want to give a clear message about what we do. We do dashboards, we create beautifull charts
Nice to have
• displays charts icons to let people know tha we do charts

```html
<!DOCTYPE html>
<html lang="en">
<head>
<meta charset="utf-8">
<title>Plume analytics — Business Card</title>
<link rel="stylesheet" href="https://fonts.googleapis.com/css2?family=Exo+2:wght@300;400;600;700&display=swap">
<style>
  :root {
    --bg: #2b2b2d;
    --card: #ffffff;
    --card-shade: #ececec;
    --blue: #1f9ad6;
    --blue-deep: #0f86c4;
    --graphite: #3a3b3d;
    --ink: #333438;
    --muted: #6d6f73;
  }
  * { box-sizing: border-box; margin: 0; padding: 0; }
  html, body { width: 1200px; height: 997px; overflow: hidden; }
  body {
    background: var(--bg);
    font-family: "Exo 2", sans-serif;
    display: flex;
    flex-direction: column;
    align-items: center;
    justify-content: center;
    gap: 48px;
  }
  .card {
    position: relative;
    width: 770px;
    height: 440px;
    background: radial-gradient(ellipse at 40% 35%, var(--card) 55%, var(--card-shade) 100%);
    overflow: hidden;
    box-shadow: 0 14px 30px rgba(0,0,0,.45);
  }
  .card-bands { position: absolute; inset: 0; }
  .brand {
    position: absolute;
    display: flex;
    align-items: center;
    gap: 18px;
  }
  .brand-mark {
    width: 34px; height: 34px;
    background: var(--blue);
  }
  .brand-name {
    font-weight: 400;
    font-size: 46px;
    letter-spacing: 1px;
    color: var(--blue);
    line-height: 1;
  }
  /* back */
  .card--back .brand { left: 150px; top: 180px; }
  .tagline {
    position: absolute;
    left: 500px; top: 240px;
    font-size: 13px;
    color: var(--muted);
    letter-spacing: .5px;
  }
  /* front */
  .card--front .brand { left: 70px; top: 110px; }
  .contact {
    position: absolute;
    right: 56px; top: 170px;
    width: 300px;
    text-align: right;
  }
  .contact-name {
    font-size: 22px;
    font-weight: 400;
    color: var(--blue);
    letter-spacing: 1px;
  }
  .contact-role {
    font-size: 15px;
    font-weight: 400;
    color: var(--ink);
    letter-spacing: .5px;
    padding-bottom: 6px;
    border-bottom: 2px solid var(--blue);
  }
  .contact-phone {
    margin-top: 14px;
    font-size: 16px;
    color: var(--muted);
    letter-spacing: 1px;
    display: flex;
    justify-content: flex-end;
    align-items: center;
    gap: 10px;
  }
  .phone-icon { width: 12px; height: 18px; }
  .rule {
    position: absolute;
    right: 56px; top: 290px;
    width: 360px; height: 2px;
    background: linear-gradient(90deg, rgba(31,154,214,0), var(--blue));
  }
  .address {
    position: absolute;
    right: 56px; top: 308px;
    font-size: 21px;
    font-weight: 700;
    color: var(--blue-deep);
    letter-spacing: 1px;
  }
</style>
</head>
<body>
  <section class="card card--back">
    <svg class="card-bands" viewBox="0 0 770 440" aria-hidden="true">
      <path d="M0 440 V420 H420 L430 400 H770 V440 Z" fill="var(--graphite)"/>
      <path d="M430 400 L440 372 H560 L580 340 H770 V400 Z" fill="var(--blue)"/>
    </svg>
    <div class="brand">
      <span class="brand-mark"></span>
      <span class="brand-name">Plume analytics</span>
    </div>
    <p class="tagline">Visualize your data</p>
  </section>

  <section class="card card--front">
    <svg class="card-bands" viewBox="0 0 770 440" aria-hidden="true">
      <path d="M0 440 V376 H260 L290 398 H770 V440 Z" fill="var(--blue)"/>
      <path d="M290 398 L300 356 H540 L550 398 Z" fill="var(--blue)"/>
      <path d="M560 398 L566 360 H770 V398 Z" fill="var(--graphite)"/>
    </svg>
    <div class="brand">
      <span class="brand-mark"></span>
      <span class="brand-name">Plume analytics</span>
    </div>
    <div class="contact">
      <p class="contact-name">Mathis Gervaud</p>
      <p class="contact-role">MANAGING DIRECTOR</p>
      <p class="contact-phone">+33641927508
        <svg class="phone-icon" viewBox="0 0 12 18" aria-hidden="true">
          <rect x="1" y="1" width="10" height="16" rx="2" fill="none" stroke="var(--blue)" stroke-width="1.5"/>
          <line x1="4.5" y1="14" x2="7.5" y2="14" stroke="var(--blue)" stroke-width="1.5"/>
        </svg>
      </p>
    </div>
    <div class="rule"></div>
    <p class="address">61 Orchard Lane Milbury, Vermont 05671</p>
  </section>
</body>
</html>
```